Summer Sunglass offer

Need a poster design for a spring / summer campaign. We are an opticians with good footfall. The design needs to be eye catching and aimed at 40 year old plus. The offer is Up to 50% off sunglass offer, t&c apply. (I have attached our last year campaign)
Also need a 2 sided A5 leaflet design (see attached)
I've uploaded a copy of our logo

A5 leaflet should read:

Grab a bargain on two great looks this summer Upto 50% off sunglasses
Look great and stay safe in the sun this summer

We want you to look great, feel fantastic and most of all stay safe in the sun this summer. That’s why we’re offering you 50% off prescription sunglasses with every complete pair of glasses you buy this summer or 25% off for prescription sunglasses with no other purchase.
Find you new summer looks from our gorgeous collection of frames in store. It matters to us that you look great in your new glasses as much as how well you see through them, so we’ll be on hand to help you find frames that suit you best.
What new looks will you go for? Smart or sassy? Formal or Fun? Whatever you’re in the mood for, you’ll find it in our collections this summer.
Call in today to find your new looks, and remember to bring your prescription if you don’t need an eye test.

Target Market(s)

40 + year old

Industry/Entity Type

Optician

Colors

Designer to choose colors to be used in the design.

Requirements
Must have
• Images, preferably a male and Female image

```html
<!DOCTYPE html>
<html lang="en">
<head>
<meta charset="utf-8">
<title>Summer Sunglasses Offer – Bramley Eyecare Centre</title>
<link rel="stylesheet" href="https://fonts.googleapis.com/css2?family=Bebas+Neue&family=Oswald:wght@200;300&family=Montserrat+Alternates:wght@400;500&display=swap">
<style>
  :root {
    --brand-blue: #2a56a5;
    --brand-teal: #4aa9ad;
    --summer-grey: #c9c9c9;
    --footer-grey: #b1b4b6;
    --ink: #2b2b2b;
    --white: #ffffff;
  }
  * { margin: 0; padding: 0; box-sizing: border-box; }
  html, body { width: 849px; height: 1200px; overflow: hidden; background: var(--white); }
  .poster {
    position: relative;
    width: 849px;
    height: 1200px;
    overflow: hidden;
    background: var(--white);
    font-family: "Montserrat Alternates", sans-serif;
  }
  .hero-photo {
    position: absolute;
    left: 0; top: 0;
    width: 849px; height: 900px;
    background:
      radial-gradient(ellipse 230px 420px at 330px 430px, #c9a477 0%, #d8bb93 45%, rgba(230,215,195,0) 100%),
      radial-gradient(ellipse 120px 380px at 560px 620px, rgba(196,160,115,.8) 0%, rgba(220,200,170,0) 100%),
      linear-gradient(100deg, #eef3f2 0%, #f6f8f8 40%, #e9eff2 75%, #dfe7ec 100%);
  }
  .shapes { position: absolute; left: 0; top: 0; }
  .headline-top {
    position: absolute;
    right: 42px; top: 44px;
    font-family: "Oswald", sans-serif;
    font-weight: 200;
    font-size: 57px;
    line-height: 1;
    color: var(--brand-teal);
    letter-spacing: -0.5px;
  }
  .headline-main {
    position: absolute;
    right: 40px; top: 100px;
    font-family: "Bebas Neue", sans-serif;
    font-size: 140px;
    line-height: 1;
    color: var(--summer-grey);
    letter-spacing: -1px;
  }
  .offer-upto {
    position: absolute;
    left: 1px; top: 758px;
    width: 90px;
    text-align: center;
    transform: rotate(-90deg);
    font-family: "Bebas Neue", sans-serif;
    font-size: 52px;
    line-height: 1;
    color: var(--white);
  }
  .offer-value {
    position: absolute;
    left: 70px; top: 688px;
    font-family: "Bebas Neue", sans-serif;
    font-size: 178px;
    line-height: 1;
    color: var(--white);
    letter-spacing: -2px;
  }
  .offer-percent {
    position: absolute;
    left: 221px; top: 700px;
    font-family: "Oswald", sans-serif;
    font-weight: 300;
    font-size: 64px;
    line-height: 1;
    color: var(--white);
  }
  .offer-off {
    position: absolute;
    left: 220px; top: 762px;
    font-family: "Oswald", sans-serif;
    font-weight: 200;
    font-size: 76px;
    line-height: 1;
    color: var(--brand-blue);
  }
  .offer-asterisk {
    position: absolute;
    left: 306px; top: 756px;
    font-family: "Oswald", sans-serif;
    font-weight: 200;
    font-size: 34px;
    line-height: 1;
    color: var(--brand-blue);
  }
  .offer-rule {
    position: absolute;
    left: 170px; top: 836px;
    width: 213px; height: 1px;
    background: var(--brand-teal);
  }
  .offer-product {
    position: absolute;
    left: 170px; top: 844px;
    font-size: 42px;
    line-height: 1;
    color: var(--brand-teal);
    white-space: nowrap;
  }
  .offer-product .light { font-family: "Oswald", sans-serif; font-weight: 200; font-size: 40px; }
  .offer-product .bold { font-family: "Bebas Neue", sans-serif; font-size: 46px; }
  .tagline {
    position: absolute;
    right: 45px; top: 952px;
    font-size: 19.6px;
    color: var(--brand-blue);
    white-space: nowrap;
  }
  .brand {
    position: absolute;
    right: 45px; top: 1015px;
    display: flex;
    align-items: center;
    gap: 18px;
  }
  .brand-dot {
    width: 58px; height: 58px;
    border-radius: 50%;
    background: var(--brand-teal);
  }
  .brand-name {
    font-family: "Montserrat Alternates", sans-serif;
    font-weight: 500;
    font-size: 29px;
    line-height: 1;
    color: var(--brand-blue);
    white-space: nowrap;
  }
  .web-address {
    position: absolute;
    right: 46px; top: 1107px;
    font-size: 21px;
    font-weight: 500;
    line-height: 1.4;
    color: var(--white);
  }
  .terms {
    position: absolute;
    left: 0; top: 1143px;
    width: 849px; height: 57px;
    background: var(--footer-grey);
    padding-top: 11px;
    text-align: center;
    font-size: 11.4px;
    line-height: 18px;
    color: var(--ink);
  }
</style>
</head>
<body>
<main class="poster">
  <div class="hero-photo" role="img" aria-label="Photo of a woman with long wavy blonde hair wearing dark sunglasses, resting her cheek on her hand against a bright summer background"></div>

  <svg class="shapes" width="849" height="1200" viewBox="0 0 849 1200" aria-hidden="true">
    <polygon class="chevron-band band-light" points="0,474 588,792 849,651 849,1200 0,1200" fill="#ffffff" fill-opacity="0.45"/>
    <polygon class="chevron-band band-soft" points="0,501 588,819 849,678 849,1200 0,1200" fill="#8fd3d1" fill-opacity="0.45"/>
    <polygon class="chevron-band band-mid" points="0,528 588,846 849,705 849,1200 0,1200" fill="#5ec4c0" fill-opacity="0.6"/>
    <polygon class="chevron-band band-deep" points="0,555 588,873 849,732 849,1200 0,1200" fill="#3bb3ad" fill-opacity="0.7"/>
    <polygon class="offer-triangle" points="0,555 318,729 0,900" fill="var(--brand-blue)"/>
    <polygon class="base-panel" points="0,900 318,729 588,873 849,732 849,1200 0,1200" fill="#ffffff"/>
    <polygon class="web-stripe stripe-light" points="411,1143 498,1102 530,1102 444,1143" fill="#c3c7e6"/>
    <polygon class="web-stripe stripe-mid" points="444,1143 530,1102 560,1102 474,1143" fill="#8c96cf"/>
    <polygon class="web-bar" points="474,1143 560,1102 849,1102 849,1143" fill="var(--brand-blue)"/>
  </svg>

  <h1 class="headline">
    <span class="headline-top">GET READY FOR</span>
    <span class="headline-main">SUMMER</span>
  </h1>

  <div class="offer">
    <span class="offer-upto">UP TO</span>
    <span class="offer-value">50</span>
    <span class="offer-percent">%</span>
    <span class="offer-off">OFF</span>
    <span class="offer-asterisk">*</span>
    <span class="offer-rule"></span>
    <p class="offer-product"><span class="light">FOR </span><span class="bold">SUNGLASSES</span></p>
  </div>

  <p class="tagline">Look great and stay safe in the sun this season</p>

  <div class="brand">
    <span class="brand-dot"></span>
    <span class="brand-name">Bramley Eyecare Centre</span>
  </div>

  <p class="web-address">bramleyeyecare.co.uk</p>

  <footer class="terms">
    *Offer includes frame from selected range, standard single vision lenses, tint and UV protection.<br>
    Lens upgrades available at extra cost. Offer excludes Coral Bay frames. Cannot be used with any other offer.
  </footer>
</main>
</body>
</html>
```